依頼詳細
写真挿入は無し、メニュー、営業時間も別看板がありますので記載不要です。添付のロゴとイラストを挿入してください。看板は両面ですが1デザインでも構いません。
記載項目
記載項目
⚪店名 月灯りこまち
⚪定食 お酒 または、お食事 呑み処 など(デザインとのバランスでお願いします。)
⚪お気軽にどうぞ、気軽に来店ください など(安心して気軽に入店しやすくなる1フレーズ)
⚪イラストにふき出しで発声させてください。(フレーズはお任せします。)
⚪サイズは450mm×1300mmで縦長です。納品はaiデータです。
⚪文字色、全体的なデザインはお任せですが、背景色は薄ピンクが希望色です。グラデーションも好きです。イラスト、ロゴとのバランスでお願いします。
希望イメージ
シンプル 複雑
単色 カラフル
暗い 明るい
日常 高級
遊び心 厳粛
未来的 伝統的
女性的 男性的
希望する色
納品ファイル
• イラストレーター形式 (.ai)
補足説明
私ai使えませんので確認は別形式でお願いします。
選定確約有りに変更しました。

見やすくバランスが良く丁度良いです。

また、よろしくお願いいたします。

```html
<!DOCTYPE html>
<html lang="ja">
<head>
<meta charset="utf-8">
<title>月灯りこまち 店頭看板</title>
<link rel="stylesheet" href="https://fonts.googleapis.com/css2?family=Yuji+Syuku&family=Shippori+Mincho:wght@600&family=M+PLUS+Rounded+1c:wght@500&display=swap">
<style>
  :root {
    --bg-top: #f6e3ea;
    --bg-mid: #eab8c9;
    --bg-bottom: #d98aa7;
    --sun: #e7a3b8;
    --ink: #2a2226;
    --name: #8b5a3c;
    --seal: #b8323c;
    --bubble: #f4f0e4;
    --bubble-text: #4f8c3a;
    --kimono-green: #a9cf8a;
    --kimono-pink: #e39ab6;
    --blossom-white: #fbf7fa;
    --blossom-pink: #e9bccd;
  }
  html, body {
    margin: 0;
    padding: 0;
    overflow: hidden;
  }
  .signboard {
    position: relative;
    width: 1200px;
    height: 3236px;
    overflow: hidden;
    background: linear-gradient(180deg, var(--bg-top) 0%, var(--bg-mid) 45%, var(--bg-bottom) 100%);
  }
  .backdrop-circle {
    position: absolute;
    left: 80px;
    top: 140px;
    width: 760px;
    height: 760px;
    border-radius: 50%;
    background: var(--sun);
    opacity: 0.55;
  }
  .tagline-rule {
    position: absolute;
    left: 928px;
    top: 40px;
    width: 5px;
    height: 1100px;
    background: var(--ink);
  }
  .tagline {
    position: absolute;
    left: 946px;
    top: 44px;
    writing-mode: vertical-rl;
    font-family: "Shippori Mincho", serif;
    font-weight: 600;
    font-size: 88px;
    line-height: 1;
    letter-spacing: 6px;
    color: var(--ink);
    margin: 0;
  }
  .shop-name {
    position: absolute;
    left: 90px;
    top: 110px;
    height: 1650px;
    writing-mode: vertical-rl;
    font-family: "Yuji Syuku", serif;
    font-size: 270px;
    line-height: 1.05;
    color: var(--name);
    margin: 0;
  }
  .shop-seal {
    position: absolute;
    left: 58px;
    top: 1730px;
    width: 56px;
    height: 56px;
    border: 5px solid var(--seal);
    border-radius: 8px;
    box-sizing: border-box;
  }
  .romaji {
    position: absolute;
    left: 560px;
    top: 1220px;
    margin: 0;
    font-family: "M PLUS Rounded 1c", sans-serif;
    font-weight: 500;
    font-size: 46px;
    line-height: 1.15;
    letter-spacing: 3px;
    color: var(--ink);
  }
  .mascot {
    position: absolute;
    left: 790px;
    top: 1440px;
    width: 390px;
    height: 1740px;
    border-radius: 195px 195px 60px 60px;
    background: linear-gradient(180deg, var(--kimono-pink) 0%, var(--kimono-green) 40%, var(--kimono-pink) 75%, var(--kimono-green) 100%);
    opacity: 0.85;
  }
  .speech-tail {
    position: absolute;
    border-radius: 50%;
    background: var(--bubble);
  }
  .speech-tail.large { left: 392px; top: 1778px; width: 66px; height: 66px; }
  .speech-tail.small { left: 462px; top: 1740px; width: 36px; height: 36px; }
  .speech-bubble {
    position: absolute;
    left: 100px;
    top: 1800px;
    width: 380px;
    height: 380px;
    margin: 0;
    border-radius: 50%;
    background: var(--bubble);
    display: flex;
    align-items: center;
    justify-content: center;
    text-align: center;
    font-family: "M PLUS Rounded 1c", sans-serif;
    font-weight: 500;
    font-size: 54px;
    line-height: 1.5;
    color: var(--bubble-text);
  }
  .blossoms {
    position: absolute;
    left: 70px;
    top: 2220px;
    width: 740px;
    height: 980px;
    border-radius: 46% 54% 40% 60% / 50% 44% 56% 50%;
    background: radial-gradient(circle at 50% 45%, var(--blossom-white) 0%, var(--blossom-white) 40%, var(--blossom-pink) 100%);
  }
</style>
</head>
<body>
  <main class="signboard">
    <div class="backdrop-circle"></div>

    <div class="tagline-rule"></div>
    <h2 class="tagline">お食事とお酒の楽しみ処</h2>

    <h1 class="shop-name">月灯り<br>こまち</h1>
    <div class="shop-seal"></div>
    <p class="romaji">tsukiakari<br>komachi</p>

    <div class="mascot" role="img" aria-label="着物姿で出迎える店の看板娘のイラスト"></div>

    <div class="speech-tail large"></div>
    <div class="speech-tail small"></div>
    <p class="speech-bubble">お気軽に<br>お立ち寄り<br>ください</p>

    <div class="blossoms" role="img" aria-label="大きな桜の花のイラスト"></div>
  </main>
</body>
</html>
```